Community-based social network needs a new landing page

We need a landing page for a local social network in Singapore called "LaneSharely.sg". It is a website that help neighbours to connect with each other for mutual benefits such as providing professional/non-professional services, sharing items, and neighbourly help, etc.

There is an existing website but we want to completely revamp it. It is most important that the new landing page communicates that the neighbourhood has skills and services for people to discover.

The final design of the landing page should be modern, and communicates a sense of community and vibrancy. As a matter of priority, more real estate should be accorded to the neighbours providing services elements.

We have drafted 2 reference sites that communicates the key ideas/user propositions for your easy reference:
http://tavrelko82.exampleweb.com/lanesharely
http://tavrelko82.exampleweb.com/lanesharely2

As long as the key ideas/user propositions are kept to, we are open to any design proposals. I.e. you do not have to follow the design layout of the reference sites

Target Market(s)

Our target market is primarily the Singapore community, includes all genders, education levels and occupations, aged between 17-45 years old.

In the file uploaded, you will find pictures of Singapore neighbourhoods and people of local ethnicities. Please use them, but you may arrange and add further filters to better enhance them

Industry/Entity Type

Real Estate

Requirements
Nice to have
• Landing page could be similar to that of www.gatherova.com, not just at the top, but also the way the other categories are presented at the bottom.

```html
<!DOCTYPE html>
<html lang="en">
<head>
<meta charset="utf-8">
<title>LaneSharely.sg – Discover your neighbourhood</title>
<link href="https://fonts.googleapis.com/css2?family=Oswald:wght@400;500&family=Open+Sans:wght@400;600;700&family=Cabin:wght@500&display=swap" rel="stylesheet">
<style>
:root{
  --sky:#bfe3f2;
  --sky-deep:#9fd2ea;
  --orange:#d4501c;
  --gold:#d19a1e;
  --rule:#9cc9df;
  --green:#5aa632;
  --amber:#f39a12;
  --navy:#3b5998;
  --crimson:#a3173c;
  --page-grey:#e6e6e6;
  --ink:#555;
  --dark:#333333;
  --dark-line:#474747;
  --accent-blue:#6ec3e4;
  --link:#2a8ad0;
  --white:#fff;
}
*{box-sizing:border-box;margin:0;padding:0}
html,body{width:782px;height:1200px;overflow:hidden}
body{position:relative;background:var(--page-grey);font-family:"Open Sans",Arial,sans-serif;color:var(--ink)}
.abs{position:absolute}

/* header */
.topbar{left:0;top:0;width:782px;height:65px;background:linear-gradient(180deg,var(--sky-deep),var(--sky))}
.brand{left:114px;top:18px;display:flex;align-items:center;gap:6px;font-family:"Oswald",sans-serif;font-weight:500;font-size:19px;color:#2d2d2d;letter-spacing:.3px}
.brand-dot{width:12px;height:12px;border-radius:50%;background:var(--orange)}
.btn{top:17px;height:24px;border-radius:3px;color:var(--white);font-size:11px;font-weight:600;display:flex;align-items:center;justify-content:center;white-space:nowrap;box-shadow:inset 0 -2px 0 rgba(0,0,0,.15)}
.btn-register{left:438px;width:72px;background:var(--green)}
.btn-login{left:518px;width:71px;background:var(--amber)}
.btn-social{left:598px;width:70px;background:var(--navy);font-size:8px}

.tagline-band{left:0;top:65px;width:782px;height:37px;background:var(--white)}
.tagline{right:114px;top:70px;font-family:"Cabin",sans-serif;font-weight:500;font-size:17px;color:var(--orange)}

/* hero */
.hero{left:0;top:102px;width:782px;height:270px;background:radial-gradient(ellipse at 15% 50%,#8a6a4a 0 18%,transparent 38%),linear-gradient(90deg,#6f8a3c,#9db35a 45%,#7f9a46)}
.hero-title{left:0;top:122px;width:782px;text-align:center;font-family:"Oswald",sans-serif;font-size:26px;color:var(--white);text-shadow:0 1px 3px rgba(0,0,0,.4)}
.hero-avatar{left:346px;top:172px;width:96px;height:96px;border-radius:50%;border:3px solid var(--white);background:radial-gradient(circle at 40% 40%,#c9a07a,#6e4a2e)}
.hero-sub{left:0;top:280px;width:782px;text-align:center;font-size:21px;color:var(--white);text-shadow:0 1px 3px rgba(0,0,0,.4)}
.hero-cta{left:328px;top:325px;width:128px;height:28px;background:var(--crimson);border:1px solid #7a0f2b;color:var(--white);font-family:"Oswald",sans-serif;font-size:16px;display:flex;align-items:center;justify-content:center}
.hero-arrow{top:222px}

/* categories */
.card{background:var(--white);box-shadow:0 1px 4px rgba(0,0,0,.25);padding:3px}
.card-photo{width:100%;position:relative;overflow:hidden}
.card-label{position:absolute;left:50%;top:55%;transform:translate(-50%,-50%) rotate(-38deg);font-family:"Oswald",sans-serif;font-size:17px;line-height:1.05;color:var(--white);text-align:center;text-shadow:0 0 3px #333,0 0 2px #333;white-space:nowrap}
.card-pro{left:114px;top:403px;width:137px;height:193px}
.card-pro .card-photo{height:133px;background:linear-gradient(135deg,#d9c7b0,#7b8592 60%,#3d4250)}
.card-text{font-size:8px;line-height:12px;color:#666;padding:10px 8px 0}
.stack{left:319px;top:406px;width:137px;height:136px}
.stack .card{position:absolute;inset:0}
.card-nonpro .card-photo{height:128px;background:radial-gradient(circle at 50% 50%,#e3b48f,#8c5a3c 70%)}
.card-share .card-photo{height:128px;background:linear-gradient(135deg,#6d7a6a,#b69a82 55%,#efe7dc)}

.section-title{font-family:"Oswald",sans-serif;font-size:15px;color:var(--gold);top:624px}
.section-rule{top:646px;height:1px;background:var(--rule)}

.listings{left:114px;top:668px;width:250px;height:220px;background:var(--white);border:1px solid #d8d8d8;box-shadow:0 0 0 3px #f2f2f2}
.listing{position:absolute;left:28px;display:flex;align-items:flex-start;gap:10px;font-family:Arial,sans-serif;font-size:9px;line-height:13px;color:#666;width:212px}
.listing svg{flex:none}
.view-more{position:absolute;right:11px;top:196px;font-size:8.5px;font-weight:700;color:var(--link);border-bottom:1px solid var(--link)}

.members{left:418px;top:668px;width:230px;height:146px;display:grid;grid-template-columns:repeat(8,1fr);gap:1px;background:var(--white);padding:2px;box-shadow:0 1px 3px rgba(0,0,0,.2)}
.members span{display:block}

/* footer */
.footer{left:0;top:910px;width:782px;height:284px;background:var(--dark);border-top:3px solid var(--accent-blue)}
.footer-base{left:0;top:1194px;width:782px;height:6px;background:#5a5a5a}
.footer-heading{color:var(--white);font-family:Arial,sans-serif;font-weight:700}
.share-box{left:114px;top:962px;width:329px;height:77px;background:var(--white);border-radius:3px}
.count{position:absolute;width:42px;height:20px;border:1px solid #ccc;border-radius:3px;font-size:10px;display:flex;align-items:center;justify-content:center;color:#444}
.mini-btn{position:absolute;width:42px;height:17px;border-radius:3px;color:var(--white);font-size:9px;font-weight:700;display:flex;align-items:center;justify-content:center}
.like-row{position:absolute;left:120px;top:10px;display:flex;align-items:center;gap:6px;font-size:8px;color:#555}
.like-btn{background:#5f78ab;color:var(--white);font-weight:700;padding:3px 6px;border-radius:2px;font-size:8px}
.like-row b{color:var(--link);font-weight:400}
.faces{position:absolute;left:122px;top:40px;display:flex;gap:2px}
.faces span{width:25px;height:25px;display:block}
.mention{color:var(--white);font-size:10px;font-family:Arial,sans-serif}
.footer-rule{left:114px;top:1061px;width:554px;height:1px;background:var(--dark-line)}
.footer-copy{left:114px;top:1079px;font-size:12px}
.footer-about{left:114px;top:1103px;width:180px;color:#ddd;font-family:Arial,sans-serif;font-size:7.5px;line-height:11px}
.footer-col{top:1081px;font-family:Arial,sans-serif}
.footer-col h4{color:var(--white);font-size:10px;margin-bottom:9px;white-space:nowrap}
.footer-col a{display:block;color:#ddd;font-size:8px;line-height:12px;text-decoration:none;padding-left:3px}
</style>
</head>
<body>

<header>
  <div class="abs topbar"></div>
  <div class="abs brand"><span class="brand-dot"></span>LaneSharely.sg</div>
  <a class="abs btn btn-register">Register</a>
  <a class="abs btn btn-login">Login</a>
  <a class="abs btn btn-social">Linkbook Login</a>
  <div class="abs tagline-band"></div>
  <p class="abs tagline">Use the resources of the 50,000 people living around you</p>
</header>

<section>
  <div class="abs hero" role="img" aria-label="Photo of a small puppy on green grass"></div>
  <h1 class="abs hero-title" style="font-weight:400">Mia is offering dog walking at $10 per hour</h1>
  <div class="abs hero-avatar" role="img" aria-label="Round portrait of the neighbour with her dog"></div>
  <p class="abs hero-sub">Discover services offered by trusted people and businesses</p>
  <a class="abs hero-cta">Get Started!</a>
  <svg class="abs hero-arrow" style="left:24px" width="20" height="34" viewBox="0 0 20 34"><path d="M16 3 L4 17 L16 31" fill="none" stroke="#fff" stroke-width="5" stroke-linecap="round"/></svg>
  <svg class="abs hero-arrow" style="left:740px" width="20" height="34" viewBox="0 0 20 34"><path d="M4 3 L16 17 L4 31" fill="none" stroke="#fff" stroke-width="5" stroke-linecap="round"/></svg>
</section>

<section>
  <div class="abs card card-pro">
    <div class="card-photo" role="img" aria-label="Photo of two business professionals">
      <span class="card-label">Professional<br>Services</span>
    </div>
    <p class="card-text">This is Mockshop's version of Lorem Ipsum. Proin gravi-da nibh vel velit auctor</p>
  </div>

  <div class="abs stack">
    <div class="card" style="transform:rotate(5deg)"></div>
    <div class="card" style="transform:rotate(-4deg)"></div>
    <div class="card card-nonpro">
      <div class="card-photo" role="img" aria-label="Photo of a group of smiling friends">
        <span class="card-label">Non-Professional<br>Services</span>
      </div>
    </div>
  </div>

  <div class="abs stack" style="left:524px;top:408px">
    <div class="card" style="transform:rotate(4deg)"></div>
    <div class="card" style="transform:rotate(-3deg)"></div>
    <div class="card card-share">
      <div class="card-photo" role="img" aria-label="Photo of two people shaking hands">
        <span class="card-label">Share &amp; Help</span>
      </div>
    </div>
  </div>

  <h2 class="abs section-title" style="left:114px;font-weight:400">Latest listings</h2>
  <div class="abs section-rule" style="left:114px;width:250px"></div>
  <h2 class="abs section-title" style="left:418px;font-weight:400">Latest registered users</h2>
  <div class="abs section-rule" style="left:418px;width:250px"></div>

  <div class="abs listings">
    <div class="listing" style="top:24px">
      <svg width="18" height="12" viewBox="0 0 18 12"><rect x="1" y="1" width="16" height="10" rx="1" fill="#5d9bd3"/><rect x="3" y="4" width="5" height="4" fill="#fff"/></svg>
      <span>KelvinL is selling Micro/Neno sim Adapters</span>
    </div>
    <div class="listing" style="top:53px">
      <svg width="18" height="16" viewBox="0 0 18 16"><path d="M11 1 L5 9 H9 L7 15 L13 6 H9 Z" fill="#d94f86"/></svg>
      <span>PKS wants to offer Electrical Repair (DIY)</span>
    </div>
    <div class="listing" style="top:86px">
      <svg width="18" height="18" viewBox="0 0 18 18"><rect x="4" y="8" width="10" height="8" rx="1" fill="#7cb342"/><path d="M14 10 L17 6" stroke="#7cb342" stroke-width="2"/><path d="M6 8 Q9 3 12 8" fill="none" stroke="#7cb342" stroke-width="1.5"/></svg>
      <span>Ben Tan wants to offer I can help water your plants while you are overseas! I am de-pendable and detailed</span>
    </div>
    <div class="listing" style="top:140px">
      <svg width="18" height="22" viewBox="0 0 18 22"><path d="M5 1 L2 21 M13 1 L16 21 M4 6 H14 M3.5 11 H14.5 M3 16 H15" stroke="#e0672d" stroke-width="1.6" fill="none"/></svg>
      <span>FarahN has shared Ladder</span>
    </div>
    <div class="listing" style="top:170px">
      <svg width="18" height="18" viewBox="0 0 18 18"><rect x="1" y="3" width="12" height="6" rx="1" fill="#7f8c9c"/><rect x="13" y="5" width="4" height="2" fill="#7f8c9c"/><rect x="5" y="9" width="4" height="8" fill="#7f8c9c"/></svg>
      <span>FarahN has shared Electric Drill</span>
    </div>
    <a class="view-more">VIEW MORE</a>
  </div>

  <div class="abs members" role="img" aria-label="Grid of profile pictures of newly registered neighbours">
    <span style="background:#8a7a6a"></span><span style="background:#d8d2c8"></span><span style="background:#5b6a7a"></span><span style="background:#b8b8b8"></span><span style="background:#6a3a7a"></span><span style="background:#c99a6a"></span><span style="background:#9a8a6a"></span><span style="background:#dcdcdc"></span>
    <span style="background:#7a6a5a"></span><span style="background:#aa8a7a"></span><span style="background:#4a4a4a"></span><span style="background:#6a8aaa"></span><span style="background:#c45a3a"></span><span style="background:#8a5a4a"></span><span style="background:#b89a6a"></span><span style="background:#5a5a4a"></span>
    <span style="background:#3a5a3a"></span><span style="background:#caa07a"></span><span style="background:#6a6a8a"></span><span style="background:#9a6a5a"></span><span style="background:#e0a08a"></span><span style="background:#7a8a5a"></span><span style="background:#b07a6a"></span><span style="background:#8aa0b0"></span>
    <span style="background:#5a7a9a"></span><span style="background:#c07a8a"></span><span style="background:#2a2a2a"></span><span style="background:#9a5a8a"></span><span style="background:#d0c070"></span><span style="background:#7a7a7a"></span><span style="background:#6a4a3a"></span><span style="background:#303030"></span>
    <span style="background:#9a8a7a"></span><span style="background:#e08030"></span><span style="background:#4a4a3a"></span><span style="background:#6a7a8a"></span><span style="background:#b0906a"></span><span style="background:#c0a080"></span><span style="background:#a04a2a"></span><span style="background:#e09a30"></span>
  </div>
</section>

<footer>
  <div class="abs footer"></div>
  <p class="abs footer-heading" style="left:114px;top:934px;font-size:12.5px">If you found LaneSharely.sg useful, tell your friends about it!</p>

  <div class="abs share-box">
    <div class="count" style="left:12px;top:10px">853</div>
    <div class="mini-btn" style="left:12px;top:35px;background:#2fa4dc">Share</div>
    <div class="count" style="left:66px;top:10px">224</div>
    <div class="mini-btn" style="left:66px;top:35px;background:#555">+1</div>
    <div class="like-row"><span class="like-btn">Like</span><span>You, <b>Mei Lin</b> and 423 <b>Others</b> Like this</span></div>
    <div class="faces" role="img" aria-label="Small profile pictures of friends who liked the page">
      <span style="background:#8a7a6a"></span><span style="background:#4a4a4a"></span><span style="background:#c09070"></span><span style="background:#6a6a7a"></span><span style="background:#a08070"></span><span style="background:#2a2a2a"></span><span style="background:#7a5a4a"></span>
    </div>
  </div>

  <p class="abs footer-heading" style="left:504px;top:934px;font-size:12px">Media Mentions</p>
  <span class="abs mention" style="left:506px;top:958px">Lorem ipsume</span>
  <span class="abs mention" style="left:578px;top:965px">Lorem ipsume</span>
  <span class="abs mention" style="left:513px;top:983px">Lorem ipsume</span>
  <span class="abs mention" style="left:588px;top:985px">Lorem ipsume</span>

  <div class="abs footer-rule"></div>
  <p class="abs footer-heading footer-copy">© Kampongly Pte Ltd 2013</p>
  <p class="abs footer-about">This is Mockshop's version of Lorem Ipsum. Proin gravida nibh vel velit auctor aliquet. Aenean sollicitudin, lorem quis bibendum auctor, nisi elit consequat ipsum, nec sagittis sem nibh id elit. Duis sed odio sit amet nibh vulputate cursus a sit amet</p>

  <nav class="abs footer-col" style="left:353px"><h4>What to know more?</h4><a>About us</a><a>FAQs</a></nav>
  <nav class="abs footer-col" style="left:488px"><h4>Using Lane Sharely</h4><a>Terms of Use</a><a>Privacy Policy</a></nav>
  <nav class="abs footer-col" style="left:617px"><h4>Get n touch</h4><a>Contact Us</a><a>Linkbook</a></nav>
  <div class="abs footer-base"></div>
</footer>

</body>
</html>
```